Business card for event manager / organizer "velmora tandem"

Draft of a new valuable business card for my company.
Events, personnel service providers, festivals

```html
<!DOCTYPE html>
<html lang="de">
<head>
<meta charset="utf-8">
<title>velmora tandem – Visitenkarte</title>
<link rel="stylesheet" href="https://fonts.googleapis.com/css2?family=Roboto+Slab:wght@300;400;700&family=Exo+2:wght@300&display=swap">
<style>
  :root {
    --stage: #e9e6e3;
    --card-light: #ffffff;
    --card-dark: #241f23;
    --ink: #111111;
    --ink-light: #f4f1ee;
    --orange: #e8731e;
    --photo-dark: #161616;
    --photo-light: #d9d9d9;
  }
  * { box-sizing: border-box; margin: 0; padding: 0; }
  html, body {
    width: 1200px; height: 801px; overflow: hidden;
    background: var(--stage);
  }
  .stage { position: relative; width: 1200px; height: 801px; }

  .card {
    position: absolute;
    width: 540px; height: 340px;
    border-radius: 22px;
    overflow: hidden;
    box-shadow: 0 10px 28px rgba(0,0,0,.18);
  }

  /* Front */
  .card--front { left: 40px; top: 150px; background: var(--card-light); }
  .front__photo {
    position: absolute; left: 40px; top: 60px; width: 200px; height: 280px;
    background: linear-gradient(180deg, var(--photo-light) 0%, #8a8a8a 30%, var(--photo-dark) 70%, #000 100%);
  }
  .front__brand {
    position: absolute; left: 262px; top: 146px; width: 262px;
  }
  .brand-line { display: flex; align-items: center; gap: 10px; }
  .brand-mark {
    width: 30px; height: 30px; background: var(--orange); flex: none;
  }
  .brand-name {
    font-family: "Roboto Slab", Georgia, serif; font-weight: 700;
    font-size: 25px; color: var(--ink); line-height: 1;
    white-space: nowrap;
  }
  .front__tagline {
    margin-top: 12px;
    font-family: "Exo 2", Arial, sans-serif; font-weight: 300;
    font-size: 12.5px; color: var(--ink);
    white-space: nowrap;
  }

  /* Back */
  .card--back { left: 620px; top: 310px; background: var(--card-dark); }
  .back__brand {
    position: absolute; left: 34px; top: 118px; width: 210px;
    display: flex; flex-direction: column; align-items: flex-start; gap: 14px;
  }
  .back__brand .brand-mark { width: 60px; height: 60px; }
  .back__brand .brand-name { color: var(--ink-light); font-size: 23px; }

  .back__contact {
    position: absolute; left: 262px; top: 64px; width: 262px;
    font-family: "Roboto Slab", Georgia, serif; color: var(--ink-light);
  }
  .contact__name { font-size: 23px; font-weight: 400; letter-spacing: .5px; line-height: 1.1; white-space: nowrap; }
  .contact__role { font-size: 14px; color: var(--orange); margin-bottom: 14px; }
  .contact__list { list-style: none; }
  .contact__list li {
    display: flex; align-items: center; gap: 10px;
    font-size: 13px; font-weight: 300; line-height: 1.75;
    white-space: nowrap;
  }
  .contact__icon { width: 12px; height: 12px; flex: none; fill: var(--orange); }
</style>
</head>
<body>
<main class="stage">

  <section class="card card--front">
    <div class="front__photo" role="img" aria-label="Foto: Kellner in Weste und Fliege mit Tablett und zwei Sektgläsern"></div>
    <div class="front__brand">
      <div class="brand-line">
        <span class="brand-mark"></span>
        <span class="brand-name">velmora tandem</span>
      </div>
      <p class="front__tagline">..weil jedes Fest gute Gastgeber braucht!</p>
    </div>
  </section>

  <section class="card card--back">
    <div class="back__brand">
      <span class="brand-mark"></span>
      <span class="brand-name">velmora tandem</span>
    </div>
    <div class="back__contact">
      <h1 class="contact__name">JONAS BRENNER</h1>
      <p class="contact__role">Inhaber</p>
      <ul class="contact__list">
        <li><svg class="contact__icon" viewBox="0 0 12 12"><path d="M2.5 1 L4.5 1 L5.2 3.6 L4 4.5 Q5 6.8 7.5 8 L8.4 6.8 L11 7.5 L11 9.5 Q10.5 11 9 11 Q1 10 1 3 Q1 1.5 2.5 1Z"/></svg>0241 555 27 18</li>
        <li><svg class="contact__icon" viewBox="0 0 12 12"><path d="M3 0.5h6a1 1 0 0 1 1 1v9a1 1 0 0 1-1 1H3a1 1 0 0 1-1-1v-9a1 1 0 0 1 1-1Zm0.8 1.5v7h4.4V2Zm2.2 7.6a.6.6 0 1 0 0 1.2a.6.6 0 1 0 0-1.2Z"/></svg>0170 555 43 21</li>
        <li><svg class="contact__icon" viewBox="0 0 12 12"><path d="M11.5 0.5 L0.5 5.5 L4.5 7 L6 11.5 Z"/></svg>info@velmora-tandem.de</li>
        <li><svg class="contact__icon" viewBox="0 0 12 12"><path d="M6 0.5a5.5 5.5 0 1 0 0 11a5.5 5.5 0 1 0 0-11Zm0 1.3a4.2 4.2 0 0 1 0 8.4a4.2 4.2 0 0 1 0-8.4Zm-.7 1v6.4h1.4V2.8Zm-2.5 2.5v1.4h6.4V5.3Z"/></svg>velmora-tandem.de</li>
        <li><svg class="contact__icon" viewBox="0 0 12 12"><path d="M6 0.5a4 4 0 0 0-4 4c0 3 4 7 4 7s4-4 4-7a4 4 0 0 0-4-4Zm0 2.3a1.7 1.7 0 1 1 0 3.4a1.7 1.7 0 1 1 0-3.4Z"/></svg>Lindenweg 12, 52062 Aachen</li>
        <li><svg class="contact__icon" viewBox="0 0 12 12"><circle cx="6" cy="6" r="5.5"/></svg>/velmoratandem</li>
      </ul>
    </div>
  </section>

</main>
</body>
</html>
```